Massage-Creme label for a young pharmacy

We are a young pharmacy which is part of a big union. We developed for a customer a very good massage creme with aloe vera, coconut oil, and many more advantages and as well a massage jelly. All we need is a good and affordable label which is beatiful and helps us to promote our product. As we want to develop further products, it would be very cool to have a corporate label for all upcoming products.

Target Market(s)

professional masseurs and physiotherapists

Industry/Entity Type

Health And Wellness

Font styles to use
Sans Serif
Decorative

Colors

Designer to choose colors to be used in the design.

Requirements
Must have
• Professionally looking design (but I'm sure you are doing so... :-)
Nice to have
• Label can have any shape. What you see is just a bad label with corresponding sizes, so you can imagine how it would look like in the final state.
Should not have
• If possible, the label should not be completely black (although it might look cool) as we are printing it on our own Varnick tq318-dm and black is difficult to print (and very costy).

```html
<!DOCTYPE html>
<html lang="en">
<head>
<meta charset="UTF-8">
<title>Massage Crème Label</title>
<link rel="stylesheet" href="https://fonts.googleapis.com/css2?family=Playfair+Display:wght@500&family=Raleway:wght@400&display=swap">
<style>
  :root {
    --page-bg: #f2f2f2;
    --label-bg: #ffffff;
    --ink: #1d1d1d;
    --band: #2d2b2b;
    --band-text: #ffffff;
    --aloe-light: #8cc63f;
    --aloe-dark: #1f6b2e;
    --coconut: #7a4a2a;
  }
  html, body {
    margin: 0;
    padding: 0;
    width: 1200px;
    height: 1200px;
    overflow: hidden;
    background: var(--page-bg);
  }
  .canvas {
    position: relative;
    width: 1200px;
    height: 1200px;
  }
  .label {
    position: absolute;
    left: 290px;
    top: 80px;
    width: 620px;
    height: 1040px;
    background: var(--label-bg);
    box-shadow: 0 2px 14px rgba(0,0,0,0.08);
    display: flex;
    flex-direction: column;
    align-items: center;
  }
  .product-name {
    margin: 300px 0 0;
    font-family: "Playfair Display", serif;
    font-weight: 500;
    font-size: 66px;
    line-height: 1.1;
    color: var(--ink);
    text-align: center;
  }
  .ingredients {
    margin-top: 70px;
    font-family: "Playfair Display", serif;
    font-weight: 500;
    font-size: 52px;
    line-height: 1.18;
    text-align: center;
    color: var(--ink);
  }
  .ingredient-art {
    margin-top: auto;
    width: 620px;
    height: 260px;
    background: linear-gradient(100deg, var(--aloe-light) 0%, var(--aloe-dark) 55%, var(--coconut) 100%);
    opacity: 0.9;
  }
  .volume-band {
    width: 620px;
    height: 150px;
    background: var(--band);
    display: flex;
    align-items: flex-end;
    justify-content: center;
    padding-bottom: 34px;
    box-sizing: border-box;
  }
  .volume {
    font-family: "Raleway", sans-serif;
    font-weight: 400;
    font-size: 40px;
    line-height: 1;
    color: var(--band-text);
  }
</style>
</head>
<body>
  <main class="canvas">
    <section class="label">
      <h1 class="product-name">Masage Crème</h1>
      <div class="ingredients">Coconut<br>Aloe Vera</div>
      <div class="ingredient-art" role="img" aria-label="Illustration of aloe vera leaves with halved coconuts and palm fronds"></div>
      <div class="volume-band">
        <span class="volume">1000 ml</span>
      </div>
    </section>
  </main>
</body>
</html>
```